Wholistic Health Clinic (Chiropractic Osteopathic Naturapathic Homeopathic New Website Design

Create a beautiful website for Tallowmere Chiropractic clinic that has been in the Sutherland Shire for over 40 years, that exemplifies the passion for helping people with their health goals using that may include a variety of techniques including Chiropractic, Osteopathy, Acupuncture, Applied Kinesiology, Retained Neonatal Reflexes, Nutritional Advice, Exercise Prescription, Decompression therapy, Massage and Stress management techniques.
We have a wholistic approach that includes Nutritional, Emotional and Physical health

(A more detailed draft will be supplied shortly)

Pages:
Home page
About Us Page
Team Page
Contact page
Terms of service Page
Privacy Page
and any other relevant page(s)

Will supply photos for:
- The Team Page and their qualifications & brief resume
- About Us page

Will supply logos for:
NRB
PLUVEX
VITALOAN
JOBSHIELD
MVA
KPO

Target Market(s)

main target Parents of young children and those 20's to 60's who live in the Sutherland Shire & have disposable income (that said almost everybody would benefit from their services)

Coding

Coded - Design and coding required

Number of Pages Required

5+ page

Font styles to use
Sans Serif

Requirements
Must have
• Please follow the brief

1. Easy to manage ourselves to add alerts (like Covid 19 compliance & Posture fortnight etc.) & update content like photos of team members etc.
2. Must be responsive and look good on mobile devices
3. must be fast loading
4. Logo on every page
5. Easy navigation on every page
6. Phone number must be clickable
7. Terms of service & Privacy pages
8. Slider on page 1 using photo of healthy people of all ages enjoying various lifestyles & ability to add other photos easily
Should not have
• no testimonials or any non compliant elements according to the NRB

```html
<!DOCTYPE html>
<html lang="en">
<head>
<meta charset="utf-8">
<title>Meridian Pelvic Health Physiotherapy &amp; Rehab Clinic</title>
<link href="https://fonts.googleapis.com/css2?family=Raleway:wght@500;600;700&family=Open+Sans:wght@400;600&family=Roboto:wght@400;500&display=swap" rel="stylesheet">
<style>
:root{
  --blue:#1f5c99;
  --cyan:#1fa9d6;
  --purple:#a056a4;
  --purple-deep:#8a3f8f;
  --pink:#c86ad0;
  --dark:#2b2b2b;
  --footer:#3a3a3a;
  --ink:#333;
  --grey:#8a8a8a;
  --white:#fff;
}
*{margin:0;padding:0;box-sizing:border-box}
html,body{width:1200px;height:2743px;overflow:hidden;background:var(--white)}
body{position:relative;font-family:'Roboto',sans-serif;color:var(--ink)}
.abs{position:absolute}
.topbar{left:0;top:0;width:1200px;height:40px;background:var(--dark);color:#ddd;font-size:12px}
.topbar .item{top:13px;display:flex;align-items:center;gap:7px}
.topbar .social{top:12px;right:95px;display:flex;gap:22px}
.topbar .social span{width:10px;height:10px;border-radius:50%;background:#ddd;display:block;margin-top:3px}
.header{left:0;top:40px;width:1200px;height:96px}
.logo{left:90px;top:30px;font-family:'Raleway',sans-serif;font-weight:700;font-size:34px;color:var(--blue)}
.info{display:flex;gap:10px;top:32px}
.info .ring{width:36px;height:36px;border:1.5px solid var(--pink);border-radius:50%;display:flex;align-items:center;justify-content:center}
.info .label{font-size:12px;color:var(--pink);text-transform:uppercase}
.info .val{font-size:12.5px;color:#555;margin-top:3px}
.nav{left:0;top:136px;width:1200px;height:46px;background:var(--blue)}
.nav ul{list-style:none;display:flex;position:absolute;left:112px;top:15px;gap:0}
.nav li{color:var(--white);font-size:13px;margin-right:45px}
.book{right:98px;top:0;width:228px;height:46px;background:var(--dark);color:var(--white);font-size:13px;display:flex;align-items:center;justify-content:center;gap:12px}
.hero{left:0;top:182px;width:1200px;height:563px;background:linear-gradient(90deg,#e9edf0 0%,#d9e2e6 40%,#6f9ea3 60%,#c8d3d8 85%,#b7c2c8 100%)}
.hero h1{left:88px;top:177px;font-family:'Raleway',sans-serif;font-weight:700;font-size:36px;line-height:42px;color:var(--blue)}
.hero p{left:88px;top:278px;font-family:'Raleway',sans-serif;font-size:16px;line-height:19px;color:#222}
.btn{display:flex;align-items:center;justify-content:center;color:var(--white);font-size:13px}
.btn-cyan{left:88px;top:349px;width:122px;height:46px;background:var(--cyan)}
.btn-dark{left:217px;top:349px;width:121px;height:46px;background:var(--dark)}
.about h2{left:88px;top:803px;font-family:'Raleway',sans-serif;font-weight:600;font-size:20px;line-height:25px;color:#222;text-transform:uppercase}
.about .rule{left:90px;top:855px;width:48px;height:3px;background:#222}
.about h3{left:90px;top:881px;font-family:'Raleway',sans-serif;font-weight:600;font-size:21px;color:var(--blue)}
.about p{left:90px;top:910px;width:512px;font-family:'Open Sans',sans-serif;font-size:13.4px;line-height:24.5px;color:#444;letter-spacing:-.1px;hyphens:auto;-webkit-hyphens:auto}
.btn-blue{left:90px;top:1028px;width:122px;height:45px;background:var(--blue)}
.about .media{left:621px;top:799px;width:480px;height:296px;background:linear-gradient(120deg,#dfe6ea,#c9b6a8 45%,#e8d6d2 70%,#eef1f3)}
.services{left:0;top:1167px;width:1200px;height:531px;background:linear-gradient(90deg,#9a4f9f,#a75aab 45%,#a056a4)}
.sec-title{width:1200px;text-align:center;font-family:'Raleway',sans-serif;font-weight:700;font-size:32px}
.sec-sub{width:1200px;text-align:center;font-family:'Open Sans',sans-serif;font-size:14.5px}
.sec-rule{left:576px;width:48px;height:3px}
.services .sec-title{top:37px;color:var(--white)}
.services .sec-sub{top:78px;color:var(--white)}
.services .sec-rule{top:109px;background:var(--white)}
.card{width:229px;height:156px;border:1px solid rgba(255,255,255,.8);color:var(--white);text-align:center;font-family:'Raleway',sans-serif;font-weight:600;font-size:17px;letter-spacing:1px;line-height:19px;text-transform:uppercase}
.card .icon{position:absolute;left:74px;top:20px;width:80px;height:78px;border-radius:8px;background:rgba(255,255,255,.85)}
.card .name{position:absolute;left:0;width:100%;bottom:18px}
.why .sec-title{top:1728px;color:#333}
.why .sec-sub{top:1770px;color:#555}
.why .sec-rule{top:1802px;background:#333}
.circle{border-radius:50%;border:6px solid #f1f1f1;box-shadow:0 0 0 1px #e4e4e4}
.feat{text-align:center;width:260px}
.feat h4{font-family:'Raleway',sans-serif;font-weight:700;font-size:17px;color:#333}
.feat p{font-family:'Open Sans',sans-serif;font-size:12px;line-height:20px;color:var(--grey);margin-top:8px}
.footer{left:0;top:2268px;width:623px;height:475px;background:var(--footer)}
.map{left:623px;top:2268px;width:577px;height:475px;background:linear-gradient(135deg,#e4e4e4,#d2d2d2 50%,#dcdcdc)}
.mapbtn{left:632px;top:2273px;width:130px;height:26px;background:var(--white);font-size:12.5px;color:#555;display:flex;align-items:center;justify-content:center}
.contact h2{left:109px;top:2330px;font-family:'Raleway',sans-serif;font-weight:600;font-size:28px;letter-spacing:1px;color:var(--purple)}
.contact .lead{left:116px;top:2370px;font-size:15px;line-height:16px;color:#eee}
.ci{left:107px;display:flex;gap:12px;color:#eee;font-size:15px;line-height:19px}
.ci .dot{width:30px;height:30px;border-radius:50%;background:var(--purple);flex:none;display:flex;align-items:center;justify-content:center}
.ci b{font-weight:500}
.socials{left:106px;top:2615px;display:flex;gap:10px}
.socials span{width:28px;height:28px;border:1.5px solid #eee;border-radius:50%;display:block}
.copy{left:105px;top:2679px;font-size:15px;color:#eee}
.form{left:490px;top:2313px;width:256px;height:337px;background:#111}
.form h5{position:absolute;left:32px;top:13px;font-family:'Raleway',sans-serif;font-weight:600;font-size:18px;color:var(--white)}
.field{left:17px;width:222px;height:37px;background:#e6e6e6;font-size:12.5px;color:#444;display:flex;align-items:flex-start;padding:12px 10px 0;gap:8px}
.captcha{left:17px;top:230px;width:132px;height:32px;background:#f4f4f4;border:1px solid #ccc;font-size:6px;color:#555;display:flex;align-items:center;gap:5px;padding-left:6px}
.captcha i{width:11px;height:11px;border:1px solid #999;background:var(--white);display:block}
.submit{left:17px;top:280px;width:222px;height:37px;background:var(--purple);color:var(--white);font-weight:500;font-size:14px;letter-spacing:.5px}
</style>
</head>
<body>

<div class="abs topbar">
  <div class="abs item" style="left:88px">
    <svg width="12" height="12" viewBox="0 0 24 24"><path d="M6 2l4 5-2 3c1 3 3 5 6 6l3-2 5 4-3 4C10 22 2 14 2 5z" fill="none" stroke="var(--pink)" stroke-width="2"/></svg>
    Call Us : : (555) 014-2281, (555) 014-7575
  </div>
  <div class="abs item" style="left:346px">
    <svg width="14" height="11" viewBox="0 0 24 18"><rect x="1" y="1" width="22" height="16" fill="none" stroke="var(--pink)" stroke-width="2"/><path d="M1 1l11 9 11-9" fill="none" stroke="var(--pink)" stroke-width="2"/></svg>
    hello@meridianpelvic.example
  </div>
  <div class="abs social"><span></span><span></span><span></span><span></span></div>
</div>

<header class="abs header">
  <div class="abs logo">Your Logo</div>
  <div class="abs info" style="left:657px">
    <div class="ring"><svg width="16" height="18" viewBox="0 0 24 28"><path d="M12 26S3 16 3 10a9 9 0 0118 0c0 6-9 16-9 16z" fill="none" stroke="var(--pink)" stroke-width="2"/><circle cx="12" cy="10" r="3" fill="none" stroke="var(--pink)" stroke-width="2"/></svg></div>
    <div><div class="label">Our Location</div><div class="val">2831 Harbour Lane, CA 90000</div></div>
  </div>
  <div class="abs info" style="left:897px">
    <div class="ring"><svg width="18" height="18" viewBox="0 0 24 24"><circle cx="12" cy="12" r="10" fill="none" stroke="var(--pink)" stroke-width="2"/><path d="M12 6v6h5" fill="none" stroke="var(--pink)" stroke-width="2"/></svg></div>
    <div><div class="label">Working Hours</div><div class="val">Mon - Fri : 9.00 Am - 7.00 Pm</div></div>
  </div>
</header>

<nav class="abs nav">
  <ul>
    <li>Home page</li><li>About Us Page</li><li>Team Page</li><li>Contact page</li><li>Terms of service Page</li><li>Privacy Page</li>
  </ul>
  <div class="abs book">
    <svg width="20" height="20" viewBox="0 0 20 20"><rect x="1" y="3" width="18" height="16" fill="none" stroke="#fff" stroke-width="1.5"/><path d="M1 7h18M5 1v4M15 1v4M4 10h12M4 13h12M4 16h12M8 8v10M12 8v10" stroke="#fff" stroke-width="1"/></svg>
    Book Appointment Online
  </div>
</nav>

<section class="abs hero" role="img" aria-label="Photo of four smiling clinicians in scrubs and white coats standing in a bright hospital corridor">
  <h1 class="abs">Get That White Smile<br>You've Always Wanted</h1>
  <p class="abs">Amazing Results,&nbsp; The Most Effective System,<br>More Affordable Than The Dentist</p>
  <div class="abs btn btn-cyan">Get Appointment</div>
  <div class="abs btn btn-dark">Contact Us</div>
</section>

<section class="about">
  <h2 class="abs">Meridian Pelvic Health<br>Physiotherapy &amp; Rehab Clinic</h2>
  <div class="abs rule"></div>
  <h3 class="abs">The best price, service and results.</h3>
  <p class="abs">It is a primary health care profession which focuses on body mechanics. Phys&shy;iotherapy promotes healthy living and helps to prevent injury,restore function and maintain active living. This field of healthcare helps to manage both acute as well as chronic injuries using various different treatment approaches.</p>
  <div class="abs btn btn-blue">Read More</div>
  <div class="abs media" role="img" aria-label="Video still of a physiotherapist stretching a patient's leg on a treatment table"></div>
  <svg class="abs" style="left:840px;top:923px" width="50" height="50" viewBox="0 0 50 50"><circle cx="25" cy="25" r="22" fill="rgba(255,255,255,.35)" stroke="#333" stroke-width="3"/><path d="M20 15l14 10-14 10z" fill="#333"/></svg>
</section>

<section class="abs services">
  <div class="abs sec-title">OUR SERVICES</div>
  <div class="abs sec-sub">Meridian Pelvic Health Physiotherapy &amp; Rehab Clinic</div>
  <div class="abs sec-rule"></div>

  <div class="abs card" style="left:85px;top:140px"><div class="icon" role="img" aria-label="Pictogram of a therapist treating a patient"></div><div class="name">Physiotherapy</div></div>
  <div class="abs card" style="left:351px;top:140px"><div class="icon" role="img" aria-label="Pictogram of a patient on a treatment bench"></div><div class="name">Pelvic Health<br>Physiotherapy</div></div>
  <div class="abs card" style="left:618px;top:140px"><div class="icon" role="img" aria-label="Pictogram of a patient lying down with needles"></div><div class="name">TMJ Physiotherapy</div></div>
  <div class="abs card" style="left:885px;top:140px"><div class="icon" role="img" aria-label="Pictogram of hands holding a spine"></div><div class="name">Acupuncture</div></div>

  <div class="abs card" style="left:85px;top:323px"><div class="icon" role="img" aria-label="Pictogram of a bowl with leaves"></div><div class="name">Custom Orthotics</div></div>
  <div class="abs card" style="left:351px;top:323px"><div class="icon" role="img" aria-label="Pictogram of a pair of insoles"></div><div class="name">Splints &amp; Braces</div></div>
  <div class="abs card" style="left:618px;top:323px"><div class="icon" role="img" aria-label="Pictogram of a person exercising"></div><div class="name">Customized Exercise</div></div>
  <div class="abs card" style="left:885px;top:323px"><div class="icon" role="img" aria-label="Pictogram of a chiropractor treating a patient on a table"></div><div class="name">Chiropractor</div></div>
</section>

<section class="why">
  <div class="abs sec-title">WHY CHOOSE US</div>
  <div class="abs sec-sub">Meridian Pelvic Health Physiotherapy &amp; Rehab Clinic</div>
  <div class="abs sec-rule"></div>

  <svg class="abs" style="left:0;top:1860px" width="1200" height="180" viewBox="0 0 1200 180">
    <path d="M13 162C60 140 70 120 90 110M240 68C280 60 310 58 340 58M490 60C530 66 560 80 580 80M820 132C840 128 870 122 910 116M1065 78C1110 60 1150 45 1175 35" fill="none" stroke="#d8d8d8" stroke-width="1.5" stroke-dasharray="5 4"/>
    <circle cx="13" cy="162" r="4" fill="#fff" stroke="var(--purple)" stroke-width="1.5"/>
    <path d="M1178 32c-4-6-13-4-13 3 0 6 13 13 13 13s13-7 13-13c0-7-9-9-13-3z" fill="none" stroke="var(--purple)" stroke-width="1.5"/>
    <path d="M1166 35h5l3-5 3 9 3-4h7" fill="none" stroke="var(--purple)" stroke-width="1.2"/>
  </svg>

  <div class="abs circle" style="left:80px;top:1873px;width:164px;height:164px;background:linear-gradient(135deg,#8a8f93,#5b6066 60%,#c9a070)" role="img" aria-label="Photo of a therapist massaging a client's back"></div>
  <div class="abs circle" style="left:333px;top:1873px;width:164px;height:164px;background:linear-gradient(90deg,#e84d8f,#f3f3f3 45%,#5a3a6e 60%,#eee)" role="img" aria-label="Photo of exercise balls, mats and weights"></div>
  <div class="abs circle" style="left:580px;top:1833px;width:244px;height:244px;background:linear-gradient(135deg,#c8d6e0,#9fb3c4 50%,#dfe6eb)" role="img" aria-label="Photo of a physiotherapist stretching an older man's arm"></div>
  <div class="abs circle" style="left:908px;top:1873px;width:164px;height:164px;background:linear-gradient(135deg,#6a5bd6,#e3b9a0 45%,#f0f0f0)" role="img" aria-label="Photo of a woman stretching her arm"></div>

  <div class="abs feat" style="left:32px;top:2060px"><h4>Anonymity</h4><p>Sed ut perspiciatis unde omnis<br>iste natus error sit voluptatem<br>accusantium</p></div>
  <div class="abs feat" style="left:285px;top:2060px"><h4>Availability</h4><p>Sed ut perspiciatis unde omnis<br>iste natus error sit voluptatem<br>accusantium</p></div>
  <div class="abs feat" style="left:572px;top:2097px"><h4>Convenient Place</h4><p>Sed ut perspiciatis unde omnis iste natus<br>error sit voluptatem accusantium</p></div>
  <div class="abs feat" style="left:860px;top:2060px"><h4>Experience</h4><p>Sed ut perspiciatis unde omnis<br>iste natus error sit voluptatem<br>accusantium</p></div>
</section>

<footer class="contact">
  <div class="abs footer"></div>
  <div class="abs map" role="img" aria-label="Embedded street map showing the clinic location"></div>
  <div class="abs mapbtn">View larger map</div>

  <h2 class="abs">CONTACT INFO</h2>
  <div class="abs lead">Dummy text of the printing and<br>typesetting industry</div>

  <div class="abs ci" style="top:2432px">
    <div class="dot"><svg width="14" height="14" viewBox="0 0 24 24"><path d="M6 2l4 5-2 3c1 3 3 5 6 6l3-2 5 4-3 4C10 22 2 14 2 5z" fill="#fff"/></svg></div>
    <div><b>Meridian Pelvic Health Physiotherapy &amp;<br>Rehab Clinic</b><br>Unit 8, 215 Kestrel Park Blvd<br>Oakridge, ON A1A 0B2</div>
  </div>
  <div class="abs ci" style="top:2514px">
    <div class="dot"><svg width="12" height="15" viewBox="0 0 24 28"><path d="M12 26S3 16 3 10a9 9 0 0118 0c0 6-9 16-9 16z" fill="#fff"/><circle cx="12" cy="10" r="3.5" fill="var(--purple)"/></svg></div>
    <div style="padding-top:5px">(555) 014-2281,&nbsp; (555) 014-7575</div>
  </div>
  <div class="abs ci" style="top:2562px">
    <div class="dot"><svg width="14" height="11" viewBox="0 0 24 18"><rect x="1" y="1" width="22" height="16" fill="#fff"/><path d="M1 1l11 9 11-9" fill="none" stroke="var(--purple)" stroke-width="2"/></svg></div>
    <div style="padding-top:6px">hello@meridianpelvic.example</div>
  </div>
  <div class="abs socials"><span></span><span></span><span></span><span></span></div>
  <div class="abs copy">© 2018 Meridian Physio and pelvic health | All Rights Reserved.</div>

  <div class="abs form">
    <h5>GET IN TOUCH WITH US</h5>
    <div class="abs field" style="top:40px"><svg width="13" height="13" viewBox="0 0 24 24"><circle cx="12" cy="7" r="5" fill="none" stroke="#555" stroke-width="2"/><path d="M2 23c1-6 5-9 10-9s9 3 10 9" fill="none" stroke="#555" stroke-width="2"/></svg>Name</div>
    <div class="abs field" style="top:82px"><svg width="13" height="10" viewBox="0 0 24 18"><rect x="1" y="1" width="22" height="16" fill="none" stroke="#555" stroke-width="2"/><path d="M1 1l11 9 11-9" fill="none" stroke="#555" stroke-width="2"/></svg>Email</div>
    <div class="abs field" style="top:124px"><svg width="11" height="13" viewBox="0 0 20 24"><rect x="1" y="1" width="18" height="22" fill="none" stroke="#555" stroke-width="2"/><path d="M5 8h10M5 12h10M5 16h10" stroke="#555" stroke-width="2"/></svg>Subject</div>
    <div class="abs field" style="top:166px;height:56px"><svg width="14" height="13" viewBox="0 0 24 22"><path d="M2 2h14v10H8l-4 4v-4H2z" fill="#555"/><path d="M18 7h4v10h-2v4l-4-4h-6v-3" fill="#555"/></svg>Message</div>
    <div class="abs captcha"><i></i>Verify human</div>
    <div class="abs btn submit">
      <svg width="13" height="13" viewBox="0 0 24 24" style="margin-right:7px"><path d="M22 2L2 10l8 3 3 8z" fill="#fff"/></svg>SUBMIT
    </div>
  </div>
</footer>

</body>
</html>
```